I have a basketball training business combined with a strength training business. I train professio

I recently saw the cats that won the contest in the strength coach business card competition. I loved the design. I.want a card with my logo that calls attention to my clients as the card that won did to me. I would like to see if I could get a similar design. My logo is what I like although I must say I like the red and black design of the contest winner. perhaps if the smaller lettered portion of my logo coukd be separated from the larger KQT logo. It almost looks like 3M3. I like.the KQT Training and Development portion of it. I need help.

Training

```html
<!DOCTYPE html>
<html lang="en">
<head>
<meta charset="utf-8">
<title>KQT Training and Development – Business Card</title>
<link href="https://fonts.googleapis.com/css2?family=Questrial&display=swap" rel="stylesheet">
<style>
  :root {
    --backdrop: #e4e4e4;
    --card: #111214;
    --card-edge: #16171a;
    --red: #e2402f;
    --white: #ffffff;
    --muted: #4a4b4e;
  }
  * { box-sizing: border-box; margin: 0; padding: 0; }
  html, body {
    width: 1200px; height: 720px; overflow: hidden;
    background: var(--backdrop);
    font-family: "Questrial", "Century Gothic", sans-serif;
  }
  .canvas { position: relative; width: 1200px; height: 720px; }
  .card {
    position: absolute; top: 241px;
    width: 420px; height: 240px;
    background: linear-gradient(135deg, var(--card-edge), var(--card));
  }
  .card--front { left: 147px; }
  .card--back { left: 633px; }

  .brand {
    position: absolute; left: 0; right: 0;
    display: flex; align-items: center; justify-content: center; gap: 10px;
    white-space: nowrap;
  }
  .brand__square { width: 14px; height: 14px; }
  .brand__name { letter-spacing: 0.06em; text-transform: uppercase; }

  .card--front .brand { top: 108px; }
  .card--front .brand__square { background: var(--muted); }
  .card--front .brand__name { color: var(--muted); font-size: 19px; }

  .card--back .brand { top: 35px; }
  .card--back .brand__square { background: var(--white); }
  .card--back .brand__name { color: var(--white); font-size: 17px; }

  .person {
    position: absolute; top: 104px; left: 0; right: 0;
    text-align: center; color: var(--white);
  }
  .person__name {
    display: inline-block; color: var(--red); font-size: 14px;
    padding: 0 1px 1px; border-bottom: 1.5px solid var(--white);
    margin-bottom: 5px;
  }
  .person__cred { font-size: 11px; line-height: 19px; }

  .contact {
    position: absolute; top: 190px; left: 20px; right: 17px;
    display: flex; justify-content: space-between; align-items: center;
    color: var(--white); font-size: 11px; letter-spacing: 0.02em;
  }
  .contact__item { display: flex; align-items: center; gap: 5px; }
  .contact__icon { width: 12px; height: 12px; }
</style>
</head>
<body>
<div class="canvas">
  <section class="card card--front">
    <div class="brand">
      <span class="brand__square"></span>
      <span class="brand__name">KQT Training and Development</span>
    </div>
  </section>

  <section class="card card--back">
    <div class="brand">
      <span class="brand__square"></span>
      <span class="brand__name">KQT Training and Development</span>
    </div>

    <div class="person">
      <span class="person__name">Dana Whitlock</span>
      <p class="person__cred">NFTA C-PT,CES</p>
      <p class="person__cred">CSPC (Certified Strength Performance Coach)</p>
    </div>

    <div class="contact">
      <span class="contact__item">
        <svg class="contact__icon" viewBox="0 0 24 24" aria-hidden="true">
          <path fill="var(--red)" d="M6.6 10.8a15.1 15.1 0 0 0 6.6 6.6l2.2-2.2a1 1 0 0 1 1-.25 11.4 11.4 0 0 0 3.6.57 1 1 0 0 1 1 1V20a1 1 0 0 1-1 1A17 17 0 0 1 3 4a1 1 0 0 1 1-1h3.5a1 1 0 0 1 1 1c0 1.25.2 2.45.57 3.57a1 1 0 0 1-.25 1z"/>
        </svg>
        555 214 0388
      </span>
      <span class="contact__item">
        <svg class="contact__icon" viewBox="0 0 24 24" aria-hidden="true" fill="none" stroke="var(--red)" stroke-width="1.6">
          <circle cx="12" cy="12" r="10"/>
          <ellipse cx="12" cy="12" rx="4.5" ry="10"/>
          <line x1="2" y1="12" x2="22" y2="12"/>
          <line x1="4" y1="7" x2="20" y2="7"/>
          <line x1="4" y1="17" x2="20" y2="17"/>
        </svg>
        www.danawhitlockbasketball.com
      </span>
    </div>
  </section>
</div>
</body>
</html>
```